Unique Realty Niche needs a web design

Starting Note: Please do not use the colors from the logo on quickkeyhousebuyers.example which is their current website. This logo will eventually change but it is what they have now.

This website is a realty website that caters to individuals who want to rent out their homes (investors) and those who want to rent a home (Tenants). We provide no credit check to rent a home from a investor at a higher cost for the tenant to balance risk. Good renters with bad credit are able to rent or buy a house from investors who are registered in our system.

Target Market(s)

Home Owners trying to rent out their homes, and people looking to rent.

Industry/Entity Type

House

Requirements
Must have
• Main Navigation links: Home - Our Story - tenant - owner - contact us

A log in form somewhere on the page.

Key themes in the site are as follows: The site needs to be clean and professional looking i.e. no grunge. I provided some color palettes below, these are not set in stone and if you know of a good palette(s) our client is very open to all suggestions. The main navigation needs to stay on top but other on page navigations could go on left (preferably) On the left or the right will be featured listings for some homes. It will be between 3 to 5 listings showing at one time. (Please see quickkeyhousebuyers.example for example)

Example Color Palettes:
http://hueboard.example/#set/1634353
http://hueboard.example/#set/166988
http://hueboard.example/#set/1638382
http://hueboard.example/#set/1677863

Example Websites That Client Likes:
NOTE: Very Flexible, no need to duplicate these below.
http://www.oakstoneleasing.example/
http://www.bmvhomes.example/
http://www.wevakrentals.example/index.php?pr=Home_Page

Nice to have
• It would be nice to have short easy to read paragraphs accompanied by a photo so scanning is easy on the site. Then in later pages we will have more text when there is more detail needed. We know you wont come up with the content but concept would be nice.

```html
<!DOCTYPE html>
<html lang="en">
<head>
<meta charset="utf-8">
<title>Quick Key House Buyers</title>
<link rel="stylesheet" href="https://fonts.googleapis.com/css2?family=Arimo:ital,wght@0,400;0,700;1,400&family=Libre+Baskerville:wght@700&family=Yanone+Kaffeesatz:wght@300;400&family=Kalam:wght@400;700&display=swap">
<style>
:root{
  --page-dark:#2b2b2b;
  --band-light:#d9d9d9;
  --sheet:#f4f4f4;
  --panel-edge:#c9c9c9;
  --ink:#1a1a1a;
  --accent-red:#d21e1e;
  --footer-text:#e6e6e6;
}
*{box-sizing:border-box;margin:0;padding:0}
html,body{width:1200px;height:1066px;overflow:hidden}
body{position:relative;background:var(--page-dark);font-family:"Arimo",Arial,sans-serif;color:var(--ink)}
.band{position:absolute;left:0;top:160px;width:1200px;height:370px;background:var(--band-light)}
.site{position:absolute;left:200px;top:0;width:800px;height:1066px}
.header{position:absolute;left:0;top:0;width:800px;height:160px;background:linear-gradient(#ffffff,#ebebeb)}
.brand-mark{position:absolute;left:50px;top:28px;width:112px;height:112px;display:flex;align-items:center;justify-content:center;gap:6px}
.brand-mark .dot{width:14px;height:14px;border-radius:50%;background:var(--accent-red);flex:none}
.brand-mark span{font-family:"Libre Baskerville",Georgia,serif;font-size:12px;font-weight:700;line-height:1.2;color:var(--ink)}
.login{position:absolute;right:8px;top:9px;display:flex;align-items:center;gap:5px;font-size:10px;color:#444}
.login .field{width:92px;height:18px;border:1px solid #999;border-radius:9px;background:#fff;padding:2px 8px;color:#888}
.login .go{height:18px;padding:0 10px;border:1px solid #999;border-radius:3px;background:linear-gradient(#fafafa,#c9c9c9);font-weight:700;color:var(--ink);display:flex;align-items:center}
.site-title{position:absolute;left:216px;top:45px;font-family:"Libre Baskerville",Georgia,serif;font-weight:700;font-size:24px;color:#222;white-space:nowrap}
.main-nav{position:absolute;left:212px;top:114px;width:583px;height:42px;border-radius:6px;background:linear-gradient(#3a3a3a,#050505);border:2px solid #9a9a9a;display:flex;align-items:center;padding-left:8px;font-family:"Yanone Kaffeesatz",sans-serif;font-weight:300;font-size:21px;color:#fff}
.main-nav a{color:#fff;text-decoration:none}
.main-nav .active{background:linear-gradient(#fff,#d8d8d8);color:#111;border-radius:4px;padding:2px 21px;margin-right:12px}
.main-nav .sep{margin:0 30px}
.hero{position:absolute;left:0;top:160px;width:800px;height:370px;background:linear-gradient(180deg,#b8627a 0%,#e7a069 30%,#7a4a2c 65%,#1d130c 100%)}
.hero-dots{position:absolute;left:9px;top:8px;display:flex;gap:4px}
.hero-dots i{width:13px;height:13px;border-radius:50%;background:#333;border:1px solid #111}
.hero-dots i.on{background:#fff;border:3px solid #333}
.hero-tagline{position:absolute;left:21px;top:45px;font-family:"Kalam",cursive;font-weight:700;font-size:21px;line-height:20px;color:var(--accent-red);letter-spacing:1.5px}
.content{position:absolute;left:0;top:530px;width:800px;height:470px;background:var(--sheet)}
.panel{position:absolute;background:linear-gradient(#ffffff,#ececec);border:1px solid var(--panel-edge);border-radius:4px;box-shadow:0 1px 3px rgba(0,0,0,.25)}
.tab{position:absolute;background:linear-gradient(#333,#000);color:#fff;border:2px solid #aaa;border-radius:4px;font-size:16px;display:flex;align-items:center;justify-content:center;letter-spacing:.3px}
.quick-search{left:8px;top:16px;width:212px;height:200px}
.quick-search .tab{left:6px;top:4px;width:200px;height:36px}
.city-input{position:absolute;left:17px;top:52px;width:180px;height:24px;border:1px solid #777;border-radius:12px;font-size:12px;color:#777;padding:4px 10px;background:#fff}
.images-only{position:absolute;left:23px;top:87px;font-size:10px;display:flex;align-items:center;gap:11px}
.images-only b{width:11px;height:11px;border:1px solid #555;background:#fff;display:block}
.search-btn{position:absolute;left:59px;top:109px;width:95px;height:24px;border:1px solid #999;border-radius:3px;background:linear-gradient(#fafafa,#c9c9c9);font-size:13px;font-weight:700;display:flex;align-items:center;justify-content:center}
.search-links{position:absolute;left:0;top:141px;width:100%;text-align:center;font-size:12px;line-height:24px}
.search-links a{color:var(--ink);display:block}
.our-story{left:232px;top:16px;width:336px;height:202px}
.our-story .tab{left:68px;top:4px;width:198px;height:36px}
.story-text{position:absolute;left:18px;top:59px;width:302px;font-size:9.6px;line-height:12.5px}
.read-more{position:absolute;font-size:12.5px;font-style:italic}
.our-story .read-more{top:173px;right:14px}
.testimonial{position:absolute;left:20px;top:235px;width:536px}
.testimonial h3{text-align:center;color:var(--accent-red);font-size:14px;font-weight:400;margin-bottom:9px}
.testimonial p{font-family:"Kalam",cursive;font-size:12.5px;line-height:15px;letter-spacing:.9px;width:530px}
.testimonial .read-more{top:46px;right:3px}
.latest{position:absolute;left:8px;top:311px;width:560px;height:152px;background:#fafafa;border-top:1px solid #ddd}
.vtab{position:absolute;top:0;width:34px;height:152px;background:linear-gradient(90deg,#333,#000);border:2px solid #aaa;border-radius:4px;color:#fff}
.vtab span{position:absolute;left:50%;top:50%;white-space:nowrap;font-size:15px}
.vtab.left span{transform:translate(-50%,-50%) rotate(-90deg)}
.vtab.right span{transform:translate(-50%,-50%) rotate(90deg)}
.vtab.left{left:0}.vtab.right{left:522px}
.photo{position:absolute;border:2px solid #111}
.featured{left:580px;top:16px;width:212px;height:444px}
.featured .tab{left:5px;top:4px;width:200px;height:36px}
.featured .photo{left:6px;width:198px;height:92px}
.address{position:absolute;left:0;width:100%;text-align:center;font-size:14px;line-height:16px}
.footer{position:absolute;left:0;top:1000px;width:800px;height:66px;background:linear-gradient(#2e2e2e,#050505);color:var(--footer-text);font-size:10px}
.copyright{position:absolute;left:36px;top:28px}
.social{position:absolute;left:321px;top:17px;width:188px;height:32px;border-radius:10px;background:linear-gradient(#fff,#cfcfcf);display:flex;align-items:center;justify-content:center;gap:7px}
.social i{width:26px;height:26px;border-radius:6px;display:block}
.foot-nav{position:absolute;left:554px;top:28px}
</style>
</head>
<body>
<div class="band"></div>
<div class="site">
  <header class="header">
    <div class="brand-mark"><i class="dot"></i><span>Quick Key<br>House<br>Buyers</span></div>
    <form class="login" aria-label="Member log in">
      <span class="field">Username</span>
      <span class="field">Password</span>
      <span class="go">LOG IN</span>
    </form>
    <h1 class="site-title">QUICK KEY HOUSE BUYERS</h1>
    <nav class="main-nav">
      <a class="active" href="#">Home</a><span>-</span>
      <a class="sep" href="#">Our Story</a><span>-</span>
      <a class="sep" href="#">Tenant</a><span>-</span>
      <a class="sep" href="#">Owner</a><span>-</span>
      <a class="sep" href="#" style="margin-right:0">Contact Us</a>
    </nav>
  </header>

  <section class="hero" role="img" aria-label="Large two-storey villa with balconies and a pool at sunset">
    <div class="hero-dots"><i class="on"></i><i></i><i></i><i></i><i></i></div>
    <p class="hero-tagline">PICK UP THE PHONE,<br>WE'LL BUY YOUR HOME!</p>
  </section>

  <main class="content">
    <div class="panel quick-search">
      <div class="tab">QUICK SEARCH</div>
      <div class="city-input">Enter city</div>
      <div class="images-only"><b></b>Show only listings with images</div>
      <div class="search-btn">SEARCH</div>
      <div class="search-links"><a href="#">View All Listings</a><a href="#">Advanced Search</a></div>
    </div>

    <div class="panel our-story">
      <div class="tab">OUR STORY</div>
      <p class="story-text">Lorem Ipsum is simply dummy text of the printing and typesetting industry. Lorem Ipsum has been the industry's standard dummy text ever since the 1500s, when an unknown printer took a galley of type and scrambled it to make a type specimen book. It has survived not only five centuries, but also the leap into electronic typesetting, remaining essentially unchanged. It was popularised in the 1960s with the release Lorem Ipsum is simply dummy text of the printing and typesetting industry.</p>
      <span class="read-more">Read More....</span>
    </div>

    <div class="testimonial">
      <h3>What our Happy Customers have to say...</h3>
      <p>We feel they are the best property management company in Dallas, Fort Worth, and Houston.</p>
      <span class="read-more">Read More....</span>
    </div>

    <div class="latest">
      <div class="vtab left"><span>LATEST LISTINGS</span></div>
      <div class="photo" role="img" aria-label="White colonial house with red shutters and a lawn" style="left:67px;top:4px;width:197px;height:142px;background:linear-gradient(#5d8fd4 0%,#9dbce0 30%,#e9e9e9 55%,#6f8a4a 85%)"></div>
      <div class="photo" role="img" aria-label="Beige craftsman house with a front porch" style="left:297px;top:4px;width:197px;height:142px;background:linear-gradient(#3c79d0 0%,#8fb5e2 28%,#d4cdb4 55%,#4d6a34 90%)"></div>
      <div class="vtab right"><span>LATEST LISTINGS</span></div>
    </div>

    <div class="panel featured">
      <div class="tab">FEATURED LISTING</div>
      <div class="photo" role="img" aria-label="Two-storey beige family house" style="top:46px;background:linear-gradient(#c8c4e6 0%,#e4e0ea 35%,#d9ccae 65%,#6b7d4a 100%)"></div>
      <p class="address" style="top:141px">2217 Larkspur Court<br>Arlington, TX 76016</p>
      <div class="photo" role="img" aria-label="Suburban house with a garage and driveway" style="top:178px;background:linear-gradient(#8fb3d6 0%,#b9c4c8 35%,#9a8e74 60%,#5a5a55 100%)"></div>
      <p class="address" style="top:273px">3930 Halden Drive<br>Mesquite, TX 75150</p>
      <div class="photo" role="img" aria-label="Brick ranch house with a front lawn" style="top:310px;background:linear-gradient(#7fa9d8 0%,#c2d3e4 35%,#a4735a 62%,#5e7a3e 100%)"></div>
      <p class="address" style="top:405px">1184 Brannock Lane<br>Garland, TX 75040</p>
    </div>
  </main>

  <footer class="footer">
    <span class="copyright">© 2011 Quick Key House Buyers, All Rights Reserved</span>
    <div class="social" aria-label="Social links">
      <i style="background:#3b5c9a"></i><i style="background:#e8862a"></i><i style="background:#c83a8c"></i><i style="background:#3ab0d8"></i><i style="background:#2a75b0"></i>
    </div>
    <span class="foot-nav">Home - Our Story - Tenant - Owner - Contact Us</span>
  </footer>
</div>
</body>
</html>
```